Stationary Design for Stunning new Logo

I need to envelopes, letterhead, business cards designed to compliment our new logo.

We are a 25 year old printing company going through a brand refresh. All items should have the design extended to both sides for full print ability.

Industry/Entity Type

Printing

Requirements
Must have
• It must utilize the new logo & colors PMS 300 & PMS 295.

```html
<!DOCTYPE html>
<html lang="en">
<head>
<meta charset="utf-8">
<title>Clearmark Stationery Set</title>
<link href="https://fonts.googleapis.com/css2?family=Arimo:wght@400;700&family=Great+Vibes&display=swap" rel="stylesheet">
<style>
  :root {
    --pms-300: #2170c0;
    --pms-295: #173f6f;
    --paper: #f7f7f7;
    --backdrop: #ececec;
    --ink: #555a60;
    --rule: #9aa3ad;
  }
  * { margin: 0; padding: 0; box-sizing: border-box; }
  html, body { width: 1200px; height: 795px; overflow: hidden; }
  body {
    background: var(--backdrop);
    font-family: "Arimo", Arial, sans-serif;
    color: var(--ink);
    position: relative;
  }
  .piece { position: absolute; }

  .brand { font-weight: 700; color: var(--pms-300); letter-spacing: 0.04em; line-height: 1; display: flex; align-items: center; gap: 4px; }
  .brand-dot { display: inline-block; border-radius: 50%; background: var(--pms-300); }
  .tagline { color: var(--pms-300); text-transform: uppercase; letter-spacing: 0.02em; white-space: nowrap; }

  /* Letterhead */
  .letterhead { left: 291px; top: 99px; width: 293px; height: 415px; background: var(--paper); }
  .letterhead .brand { position: absolute; left: 24px; top: 22px; font-size: 17px; }
  .letterhead .brand-dot { width: 12px; height: 12px; }
  .letterhead .tagline { position: absolute; left: 40px; top: 40px; font-size: 4.6px; }
  .letter-body { position: absolute; left: 35px; top: 106px; width: 238px; font-size: 5.3px; line-height: 7.6px; }
  .letter-body p { margin-bottom: 6px; }
  .letter-body .salutation { font-weight: 700; margin-bottom: 9px; }
  .signature { position: absolute; left: 35px; top: 314px; }
  .signature .script { font-family: "Great Vibes", cursive; font-size: 15px; line-height: 16px; color: #333; }
  .signature .role { font-size: 5.3px; font-weight: 700; margin-top: 2px; }
  .letter-footer { position: absolute; left: 21px; top: 381px; font-size: 4.2px; line-height: 6px; }
  .letter-footer .row { display: flex; gap: 14px; }
  .letter-footer .web { font-weight: 700; color: var(--pms-295); }
  .letter-footer .address { border-top: 0.6px solid var(--rule); margin-top: 1px; padding-top: 1px; width: 100px; }

  /* Folder */
  .folder { left: 636px; top: 81px; width: 345px; height: 436px; background: var(--pms-300); }
  .folder .spine { position: absolute; left: 0; top: 0; width: 6px; height: 100%; background: #1d66b2; }
  .folder .brand { position: absolute; right: 28px; top: 380px; font-size: 24px; color: #fff; }
  .folder .tagline { position: absolute; right: 28px; top: 405px; font-size: 6px; color: #fff; }

  /* Business cards */
  .card { width: 132px; height: 75px; }
  .card-front { left: 187px; top: 550px; background: var(--paper); }
  .card-front .brand { position: absolute; left: 8px; top: 13px; font-size: 11px; }
  .card-front .brand-dot { width: 8px; height: 8px; }
  .card-front .tagline { position: absolute; left: 19px; top: 25px; font-size: 2.9px; }
  .card-front .person { position: absolute; left: 8px; top: 42px; font-size: 4.6px; color: var(--pms-295); }
  .card-front .person span { font-size: 3.2px; color: var(--ink); margin-left: 6px; }
  .card-front .details { position: absolute; left: 8px; top: 50px; font-size: 3px; line-height: 4.4px; }
  .card-back { left: 187px; top: 646px; background: var(--pms-300); }
  .card-back .brand { position: absolute; left: 5px; top: 55px; font-size: 11px; color: #fff; }
  .card-back .tagline { position: absolute; left: 5px; top: 67px; font-size: 2.9px; color: #fff; }

  /* DL envelope front */
  .envelope-front { left: 353px; top: 561px; width: 328px; height: 156px; background: var(--paper); }
  .envelope-front .brand { position: absolute; left: 22px; top: 9px; font-size: 15px; }
  .envelope-front .brand-dot { width: 10px; height: 10px; }
  .envelope-front .tagline { position: absolute; left: 37px; top: 26px; font-size: 3.6px; }
  .envelope-front .return { position: absolute; left: 21px; top: 134px; font-size: 3.6px; line-height: 5px; }
  .envelope-front .return .web { font-weight: 700; color: var(--pms-295); }
  .envelope-front .return .address { border-top: 0.6px solid var(--rule); width: 95px; }

  /* Envelope back */
  .envelope-back { left: 713px; top: 561px; width: 328px; height: 156px; background: var(--paper); }
  .envelope-back svg { position: absolute; left: 0; top: 0; }
  .envelope-back .brand { position: absolute; left: 0; width: 100%; top: 20px; justify-content: center; font-size: 13px; color: #fff; }
</style>
</head>
<body>

  <section class="piece letterhead" aria-label="Letterhead">
    <div class="brand"><span class="brand-dot"></span>CLEARMARK</div>
    <div class="tagline">Sharp print • Honest timing • Fair quotes for every run</div>
    <div class="letter-body">
      <p class="salutation">Lorem Ipsum,</p>
      <p>Cras mattis consectetur purus sit amet fermentum. Etiam porta sem malesuada magna mollis euismod. Integer posuere erat a ante venenatis dapibus posuere velit aliquet. Cras justo odio, dapibus ac facilisis in, egestas eget quam. Aenean eu leo quam. Pellentesque ornare sem lacinia quam venenatis vestibulum.</p>
      <p>Vivamus sagittis lacus vel augue laoreet rutrum faucibus dolor auctor. Donec sed odio dui. Etiam porta sem malesuada magna mollis euismod. Morbi leo risus, porta ac consectetur ac, vestibulum at eros. Nullam id dolor id nibh ultricies vehicula ut id elit.</p>
      <p>Donec id elit non mi porta gravida at eget metus. Fusce dapibus, tellus ac cursus commodo, tortor mauris condimentum nibh, ut fermentum massa justo sit amet risus. Cras justo odio, dapibus ac facilisis in, egestas eget quam. Cum sociis natoque penatibus et magnis dis parturient montes, nascetur ridiculus mus.</p>
      <p>Cum sociis natoque penatibus et magnis dis parturient montes, nascetur ridiculus mus. Curabitur blandit tempus porttitor. Aenean lacinia bibendum nulla sed consectetur. Lorem ipsum dolor sit amet, consectetur adipiscing elit.</p>
      <p>Cras justo odio, dapibus ac facilisis in, egestas eget quam. Morbi leo risus, porta ac consectetur ac, vestibulum at eros. Duis mollis, est non commodo luctus, nisi erat porttitor ligula, eget lacinia odio sem nec elit. Integer posuere erat a ante venenatis dapibus posuere velit aliquet. Vivamus sagittis lacus vel augue laoreet rutrum faucibus dolor auctor.</p>
    </div>
    <div class="signature">
      <div class="script">Your Name</div>
      <div class="role">Company Director</div>
    </div>
    <div class="letter-footer">
      <div class="row"><span>T: +352 40 20 11 500</span><span>F: +352 40 20 11 501</span></div>
      <div class="row"><span>E: info@clearmark-print.com</span><span class="web">www.clearmark-print.com</span></div>
      <div class="address">12, Rue des Ateliers, Northvale, L-2200 Country</div>
    </div>
  </section>

  <section class="piece folder" aria-label="Presentation folder">
    <div class="spine"></div>
    <div class="brand">CLEARMARK</div>
    <div class="tagline">Sharp print • Honest timing • Fair quotes for every run</div>
  </section>

  <section class="piece card card-front" aria-label="Business card front">
    <div class="brand"><span class="brand-dot"></span>CLEARMARK</div>
    <div class="tagline">Sharp print • Honest timing • Fair quotes for every run</div>
    <div class="person">Lena Marsh<span>Executive Director</span></div>
    <div class="details">
      T: +352 40 20 11 500 &nbsp;&nbsp; F: +352 40 20 11 501<br>
      E: lmarsh@clearmark-print.com &nbsp; <b>www.clearmark-print.com</b><br>
      12, Rue des Ateliers, Northvale, L-2200 Country
    </div>
  </section>

  <section class="piece card card-back" aria-label="Business card back">
    <div class="brand">CLEARMARK</div>
    <div class="tagline">Sharp print • Honest timing • Fair quotes for every run</div>
  </section>

  <section class="piece envelope-front" aria-label="DL envelope front">
    <div class="brand"><span class="brand-dot"></span>CLEARMARK</div>
    <div class="tagline">Sharp print • Honest timing • Fair quotes for every run</div>
    <div class="return">
      <div class="web">www.clearmark-print.com</div>
      <div class="address">12, Rue des Ateliers, Northvale, L-2200 Country</div>
    </div>
  </section>

  <section class="piece envelope-back" aria-label="DL envelope back">
    <svg width="328" height="156" viewBox="0 0 328 156" aria-hidden="true">
      <path d="M0 0 H328 L322 54 H6 Z" fill="var(--pms-300)"/>
    </svg>
    <div class="brand">CLEARMARK</div>
  </section>

</body>
</html>
```